Use Existing Logo to Design Letterhead, Envelope and Presentation Folder

We are a storm shelter company based out of Oklahoma City. We have an existing logo and brand image. We are looking for professionally designed letterhead, mailing envelopes and folders using our brand guidelines (attached). The font to be used is Futura.

The image represents simple professionalism.
We compete on quality, not price.
We value attention to detail and craftsmanship in our work.
The colors and layout are bold and clean.

Again, this is for:
1) Letterhead - contains name, address, phone, fax, and website address
2) Envelopes - logo, tagline and return address
3) Presentation Folders - logo and tag line

Our tag line is:
"Reliable Tornado-Ready Storm Shelters and Dependable Home Safety Gear"

Please submit your designs and once we have the initial layouts, we will provide the top designers with our contact information.

Good luck!

```html
<!DOCTYPE html>
<html lang="en">
<head>
<meta charset="utf-8">
<title>Keystone Shelters Stationery</title>
<link href="https://fonts.googleapis.com/css2?family=Jost:wght@400;500&display=swap" rel="stylesheet">
<style>
  :root {
    --backdrop: #46131f;
    --paper: #ffffff;
    --brand-blue: #2e3192;
    --flap-grey: #939498;
    --ink: #555555;
    --faint-grey: #ececec;
    --faint-lilac: #dcdcf0;
    --rule: #9a9a9a;
  }
  * { box-sizing: border-box; margin: 0; padding: 0; }
  html, body {
    width: 1200px; height: 680px; overflow: hidden;
    background: var(--backdrop);
    font-family: "Jost", "Futura", sans-serif;
  }
  .stage { position: relative; width: 1200px; height: 680px; }

  .sheet, .envelope { position: absolute; background: var(--paper); overflow: hidden; }

  /* Wordmark */
  .wordmark {
    display: flex; align-items: center; gap: 6px;
    color: var(--brand-blue); font-weight: 500; letter-spacing: 0.04em;
    line-height: 1.1; text-transform: uppercase; white-space: nowrap;
  }
  .wordmark__square { width: 10px; height: 10px; background: var(--brand-blue); flex: none; }
  .wordmark--light { color: var(--paper); }
  .wordmark--light .wordmark__square { background: var(--paper); }

  /* Faint corner block */
  .corner-block { position: absolute; background: var(--faint-grey); }
  .corner-band { position: absolute; background: var(--faint-lilac); }

  /* Letterhead */
  .letterhead { left: 39px; top: 33px; width: 478px; height: 619px; }
  .letterhead .wordmark { position: absolute; left: 17px; top: 52px; font-size: 15px; }
  .contact {
    position: absolute; left: 354px; top: 26px;
    border-left: 1px solid var(--rule); padding-left: 8px;
    font-size: 7.5px; color: var(--ink); line-height: 1.45;
  }
  .contact__row { display: flex; align-items: center; gap: 4px; }
  .contact__icon { width: 7px; height: 7px; flex: none; }
  .contact__address { margin-top: 5px; }
  .letterhead .corner-block { left: 300px; top: 330px; width: 178px; height: 289px; }
  .letterhead .corner-band { left: 324px; top: 420px; width: 154px; height: 70px; }
  .tagline {
    position: absolute; left: 15px; bottom: 6px;
    font-size: 9.5px; font-weight: 500; letter-spacing: 0.05em; color: var(--brand-blue);
    white-space: nowrap;
  }

  /* Envelopes */
  .envelope { width: 534px; height: 239px; }
  .envelope--back { left: 636px; top: 137px; }
  .envelope--grey-flap { left: 609px; top: 259px; }
  .envelope--front { left: 579px; top: 367px; }
  .flap { position: absolute; left: 0; top: 0; width: 534px; height: 110px; }
  .envelope .wordmark--flap {
    position: absolute; left: 50%; top: 48px; transform: translateX(-50%);
    font-size: 12px;
  }
  .envelope--front .wordmark { position: absolute; left: 9px; top: 56px; font-size: 15px; }
  .return-address {
    position: absolute; left: 9px; top: 90px;
    font-size: 7.5px; color: var(--ink); line-height: 1.35;
  }
  .envelope-url {
    position: absolute; left: 9px; bottom: 10px;
    font-size: 9.5px; letter-spacing: 0.06em; color: var(--ink);
  }
  .envelope--front .corner-block { left: 380px; top: 60px; width: 154px; height: 179px; }
  .envelope--front .corner-band { left: 436px; top: 112px; width: 98px; height: 48px; }
</style>
</head>
<body>
<main class="stage">

  <section class="sheet letterhead" aria-label="Letterhead">
    <div class="wordmark"><span class="wordmark__square"></span>Keystone Shelters</div>
    <div class="contact">
      <div class="contact__row">
        <svg class="contact__icon" viewBox="0 0 10 10"><circle cx="5" cy="5" r="5" fill="#2e3192"/><path d="M3.2 2.6 L4.3 2.4 L4.7 3.8 L4 4.3 Q4.6 5.6 5.8 6.1 L6.3 5.4 L7.6 5.8 L7.4 6.9 Q5.6 7.6 3.8 5.7 Q2.6 4.2 3.2 2.6Z" fill="#fff"/></svg>
        <span>012-345-6789</span>
      </div>
      <div class="contact__row">
        <svg class="contact__icon" viewBox="0 0 10 10"><circle cx="5" cy="5" r="5" fill="#2e3192"/><circle cx="5" cy="5" r="3" fill="none" stroke="#fff" stroke-width="0.8"/><line x1="2" y1="5" x2="8" y2="5" stroke="#fff" stroke-width="0.8"/><ellipse cx="5" cy="5" rx="1.3" ry="3" fill="none" stroke="#fff" stroke-width="0.8"/></svg>
        <span>www.keystoneshelters.com</span>
      </div>
      <div class="contact__address">Street Name, City Name<br>Zip Code - 12345</div>
    </div>
    <div class="corner-block"></div>
    <div class="corner-band"></div>
    <p class="tagline">Reliable Tornado-Ready Storm Shelters and Dependable Home Safety Gear</p>
  </section>

  <section class="envelope envelope--back" aria-label="Envelope back">
    <svg class="flap" viewBox="0 0 534 110"><path d="M2 0 Q10 40 40 48 L250 93 Q270 97 290 93 L495 48 Q525 40 532 0" fill="none" stroke="#8a8a8a" stroke-width="1"/></svg>
    <div class="wordmark wordmark--flap"><span class="wordmark__square"></span>Keystone Shelters</div>
  </section>

  <section class="envelope envelope--grey-flap" aria-label="Envelope back with grey flap">
    <svg class="flap" viewBox="0 0 534 110"><path d="M0 0 L534 0 Q528 38 500 46 L285 92 Q266 96 247 92 L36 46 Q8 38 0 0Z" fill="#939498"/></svg>
    <div class="wordmark wordmark--flap wordmark--light"><span class="wordmark__square"></span>Keystone Shelters</div>
  </section>

  <section class="envelope envelope--front" aria-label="Envelope front">
    <div class="wordmark"><span class="wordmark__square"></span>Keystone Shelters</div>
    <p class="return-address">Street Name, City Name<br>Zip Code - 12345</p>
    <div class="corner-block"></div>
    <div class="corner-band"></div>
    <p class="envelope-url">www.keystoneshelters.com</p>
  </section>

</main>
</body>
</html>
```